We need a poster design that can also be used as cover art for the 2012 Pervasive Study Summit (8.5inx11in). The event focuses on the uses of technologies in learning, from mobile phones to laptops, mp3 players to cameras. We bring together scholars, students, and practitioners to discuss classroom uses of technology, but also on the expanding possibilities of learning and education based on new, digital media.

The event is taking place in Champaign-Urbana, Illinois, one of the primary nodes in the American Midwest's "silicon prairie," a region known for its concentration of high tech companies and institutions.

We would like to see designs that highlight either the 'silicon prairie,' non-traditional learning formats, new technology, or some combination of these.

Target Market(s)

Teachers, Professors, Students, Software Developers, Educators, Technology Enthusiasts, etc.

Industry/Entity Type

Education

Requirements
Must have
• Please include the following text:
Pervasive Study
Fifth International Conference
12-13 October 2012
Larkvale Inn and Conference Center
Champaign-Urbana, Illinois

```html
<!DOCTYPE html>
<html lang="en">
<head>
<meta charset="utf-8">
<title>Pervasive Study — Fifth International Conference</title>
<link rel="stylesheet" href="https://fonts.googleapis.com/css2?family=Bebas+Neue&family=Oswald:wght@500;600;700&display=swap">
<style>
  :root {
    --navy-deep: #05071c;
    --navy: #101a5c;
    --blue-glow: #3447b8;
    --sky: #8db6e6;
    --orange: #f7941d;
  }
  html, body {
    margin: 0;
    padding: 0;
    width: 927px;
    height: 1200px;
    overflow: hidden;
    background: var(--navy-deep);
  }
  .poster {
    position: relative;
    width: 927px;
    height: 1200px;
    overflow: hidden;
    font-family: "Oswald", "Arial Narrow", sans-serif;
  }
  .keyboard-art {
    position: absolute;
    inset: 0;
    background:
      radial-gradient(ellipse 60% 40% at 78% 88%, rgba(70, 90, 210, 0.55), transparent 70%),
      radial-gradient(ellipse 45% 30% at 20% 25%, rgba(60, 80, 200, 0.45), transparent 70%),
      linear-gradient(135deg, var(--navy) 0%, var(--navy-deep) 38%, #0c1448 62%, var(--blue-glow) 100%);
  }
  .rot {
    position: absolute;
    white-space: nowrap;
    transform-origin: 0 0;
  }

  /* Title block: big name, then subtitle + accent word on the baseline side */
  .title-block {
    left: -29px;
    top: 823px;
    width: 1100px;
    transform: rotate(-47deg);
  }
  .title-main {
    margin: 0;
    padding-left: 34px;
    font-family: "Bebas Neue", "Oswald", sans-serif;
    font-weight: 400;
    font-size: 210px;
    line-height: 150px;
    height: 150px;
    letter-spacing: 34px;
    color: var(--sky);
  }
  .title-sub {
    display: flex;
    justify-content: space-between;
    align-items: flex-start;
  }
  .edition {
    padding-left: 40px;
    font-weight: 600;
    font-size: 50px;
    line-height: 58px;
    color: var(--sky);
  }
  .title-accent {
    margin-top: -18px;
    font-family: "Bebas Neue", "Oswald", sans-serif;
    font-size: 130px;
    line-height: 100px;
    letter-spacing: 6px;
    color: var(--orange);
  }

  .focus {
    margin: 0;
    left: 105px;
    top: 993px;
    transform: rotate(-46deg);
    font-weight: 700;
    font-size: 31px;
    line-height: 48px;
    color: var(--orange);
  }
  .focus span { display: block; }
  .focus .l1 { padding-left: 175px; }
  .focus .l2 { padding-left: 180px; }
  .focus .l4 { padding-left: 10px; }

  .event-details {
    margin: 0;
    left: 664px;
    top: 761px;
    transform: rotate(47deg);
    font-weight: 500;
    font-size: 28px;
    line-height: 34px;
    color: var(--sky);
  }
  .event-details span { display: block; }
  .event-details .date {
    font-weight: 700;
    font-size: 38px;
    line-height: 42px;
    color: var(--orange);
  }
</style>
</head>
<body>
<main class="poster">
  <div class="keyboard-art" role="img" aria-label="Close-up illustration of a computer keyboard lit in deep blue, keys angled across the page"></div>

  <header class="rot title-block">
    <h1 class="title-main">PERVASIVE</h1>
    <div class="title-sub">
      <span class="edition">Fifth International Conference</span>
      <span class="title-accent">STUDY</span>
    </div>
  </header>

  <p class="rot focus">
    <span class="l1">With a focus on the uses of technologies in learning,</span>
    <span class="l2">from mobile phones to laptops, mp3 players;</span>
    <span class="l3">as well as the expanding possibilities of learning</span>
    <span class="l4">and education based on new, digital media.</span>
  </p>

  <p class="rot event-details">
    <span>Pervasive Study</span>
    <span>Fifth International Conference</span>
    <span class="date">12-13 October 2012</span>
    <span>Larkvale Inn and Conference Center</span>
    <span>Champaign-Urbana, Illinois</span>
  </p>
</main>
</body>
</html>
```